Black Matte card with samurai logo which I would like it to be textured and company name on one side and on the other side I would like the company information with the kaze (Face logo) Sushi logo. Double Sided card.

Target Market(s)

majority customers are University students, University sororities and fraternities.

Industry/Entity Type

It Company

Contact Information for Business Card

Kaze Grill
317 W. Marlow Rd
Tucson, AZ 85702
Phone (520)555-0147
Fax (520)555-0193
E-mail: Kazegrillaz@mailpost.example
FB: Kazegrillaz
Twitter: Kazegrillaz

Font styles to use
Other font styles liked:
• Present Normal

```html
<!DOCTYPE html>
<html lang="en">
<head>
<meta charset="utf-8">
<title>Kaze Grill – Business Card</title>
<link rel="stylesheet" href="https://fonts.googleapis.com/css2?family=Philosopher:wght@400&display=swap">
<style>
  :root {
    --page: #ffffff;
    --card: #060606;
    --accent: #e3262c;
    --ink: #f4f4f4;
    --font-main: "Philosopher", sans-serif;
  }
  * { margin: 0; padding: 0; box-sizing: border-box; }
  html, body {
    width: 1200px;
    height: 702px;
    overflow: hidden;
    background: var(--page);
  }
  .card {
    position: absolute;
    left: 44px;
    top: 43px;
    width: 1112px;
    height: 616px;
    background: var(--card);
    font-family: var(--font-main);
    color: var(--ink);
  }
  .brand-name {
    position: absolute;
    top: 96px;
    left: 0;
    width: 100%;
    text-align: center;
    color: var(--accent);
    font-size: 64px;
    font-weight: 400;
    line-height: 1;
    letter-spacing: 2px;
  }
  .divider {
    position: absolute;
    left: 0;
    top: 220px;
    width: 100%;
    height: 5px;
    background: var(--accent);
  }
  .business-name {
    position: absolute;
    top: 264px;
    width: 100%;
    text-align: center;
    font-size: 39px;
    font-weight: 400;
    letter-spacing: 2px;
  }
  .business-address {
    position: absolute;
    top: 312px;
    width: 100%;
    text-align: center;
    font-size: 25px;
    letter-spacing: 1.6px;
  }
  .contact-list {
    position: absolute;
    list-style: none;
    font-size: 24px;
    letter-spacing: 0.8px;
  }
  .contact-list li {
    display: flex;
    align-items: center;
    height: 33px;
  }
  .contact-list svg, .contact-list .icon-square {
    flex: none;
    margin-right: 8px;
  }
  .contact-online { left: 84px; top: 476px; }
  .contact-phone { left: 804px; top: 509px; }
  .icon-square {
    width: 22px;
    height: 22px;
    background: var(--ink);
  }
</style>
</head>
<body>
  <div class="card">
    <p class="brand-name">Kaze Grill</p>

    <div class="divider"></div>

    <h1 class="business-name">Kaze Grill</h1>
    <p class="business-address">317 W. Marlow Rd Tucson, AZ 85702</p>

    <ul class="contact-list contact-online">
      <li>
        <svg width="28" height="20" viewBox="0 0 28 20" aria-label="Email">
          <rect x="0" y="0" width="28" height="20" fill="var(--ink)"/>
          <path d="M1 1 L14 12 L27 1" fill="none" stroke="var(--card)" stroke-width="2.5"/>
        </svg>
        Kazegrillaz@mailpost.example
      </li>
      <li><span class="icon-square" aria-label="Social page"></span>Kazegrillaz</li>
      <li><span class="icon-square" aria-label="Social profile"></span>Kazegrillaz</li>
    </ul>

    <ul class="contact-list contact-phone">
      <li>
        <svg width="22" height="26" viewBox="0 0 22 26" aria-label="Phone">
          <path d="M4 1 L9 1 L10 7 L7 9 Q9 15 14 19 L17 16 L21 18 L21 23 Q19 25 16 25 Q5 20 2 6 Q2 2 4 1 Z" fill="var(--ink)"/>
        </svg>
        (520)555-0147
      </li>
      <li>
        <svg width="26" height="26" viewBox="0 0 26 26" aria-label="Fax">
          <rect x="1" y="8" width="6" height="17" fill="var(--ink)"/>
          <rect x="9" y="2" width="10" height="8" fill="var(--ink)"/>
          <rect x="8" y="11" width="17" height="14" fill="var(--ink)"/>
          <g fill="var(--card)">
            <rect x="10" y="14" width="3" height="2"/><rect x="15" y="14" width="3" height="2"/><rect x="20" y="14" width="3" height="2"/>
            <rect x="10" y="18" width="3" height="2"/><rect x="15" y="18" width="3" height="2"/><rect x="20" y="18" width="3" height="2"/>
            <rect x="10" y="22" width="3" height="2"/><rect x="15" y="22" width="3" height="2"/><rect x="20" y="22" width="3" height="2"/>
          </g>
        </svg>
        (520)555-0193
      </li>
    </ul>
  </div>
</body>
</html>
```